Need a website to promote and sell my book

Using images from the book, I need a website designed that helps promote the book and eventually sell it.
*Need a landing page
*About the author page
*Storefront page to purchase
*Coming soon page
*"Featured in" page that can link to news articles etc.
The images posted here are examples, the winner of the contest will get the images from the finished book. I will provide the exact text to the winner of the contest.

I can also provide images of kids reading the book. For now, I'll just use one, the winner can have them all to choose from.
Updates

Extending deadline to allow for a few more designers to submit and to allow time for me to review and hold a poll

Target Market(s)

Parents, aunts, uncles, grandparents, friends who have kids; teachers, daycare teachers, babysitters etc.

Industry/Entity Type

Custom Publishing

Coding

Coded - Design and coding required

Number of Pages Required

5+ page

Font styles to use
Sans Serif

Colors

Designer to choose colors to be used in the design.

Requirements
Must have
• It must have a fun feel like the book.
Nice to have
• Would be great to have a section that automatically pulls tweets about the book into it.

```html
<!DOCTYPE html>
<html lang="en">
<head>
<meta charset="utf-8">
<title>Marianne — About Me</title>
<link href="https://fonts.googleapis.com/css2?family=Libre+Baskerville:ital,wght@0,400;0,700;1,400&family=Raleway:wght@300;400;500&display=swap" rel="stylesheet">
<style>
:root{
  --ink:#2b2b2b;
  --muted:#6d6d6d;
  --faint:#a9a9a9;
  --accent:#e0533a;
  --band:#f3f1ec;
  --hero:#f1efeb;
  --line:#d9c9d6;
}
*{margin:0;padding:0;box-sizing:border-box}
html,body{width:1200px;height:3193px;overflow:hidden;background:#fff}
body{position:relative;font-family:'Libre Baskerville',serif;color:var(--ink)}
.abs{position:absolute}

/* header */
.site-header{position:absolute;left:0;top:0;width:1200px;height:130px}
.nav a{position:absolute;top:58px;font-size:11px;letter-spacing:1px;color:var(--ink);text-decoration:none;text-transform:uppercase}
.nav a.active{color:var(--accent);text-decoration:underline;text-underline-offset:3px}
.logo{position:absolute;left:0;width:1200px;top:38px;text-align:center}
.logo .name{font-size:25px;letter-spacing:4px}
.logo .tag{display:inline-block;margin-top:3px;border-top:1px solid #999;padding-top:3px;font-size:8px;letter-spacing:1.5px}

/* hero */
.hero{position:absolute;left:0;top:130px;width:1200px;height:226px;background:linear-gradient(100deg,var(--hero) 0%,#efebe4 50%,#eae2d4 75%,#f2ede6 100%)}
.hero h1{position:absolute;left:159px;top:94px;font-weight:400;font-size:32px;letter-spacing:1px}
.crumb{position:absolute;right:164px;top:106px;font-style:italic;font-size:15px}
.crumb span{color:var(--accent)}

/* intro */
.intro-title{top:465px;width:1200px;text-align:center;font-size:42px;font-weight:400}
.intro-sub{top:539px;width:1200px;text-align:center;font-size:14px;color:var(--accent);text-transform:uppercase}
.intro-text{left:234px;top:574px;width:732px;text-align:center;font-size:11px;line-height:22.5px;color:var(--muted);font-family:'Raleway',sans-serif}
.pull{left:310px;top:692px;width:590px}
.pull .mark{position:absolute;left:0;top:8px;font-size:42px;color:var(--accent);font-weight:700;line-height:1}
.pull p{margin-left:40px;font-size:14px;font-weight:700;line-height:23px}
.body-text{left:162px;top:786px;width:876px;text-align:center;font-size:11px;line-height:22.5px;color:var(--muted);font-family:'Raleway',sans-serif}

/* media */
.video{left:161px;top:1038px;width:878px;height:450px;background:linear-gradient(180deg,#2a2623 0%,#5a3a33 30%,#3a2e2a 55%,#4b3b3a 80%,#2c2725 100%)}
.play{left:522px;top:1185px}
.photo-a{left:161px;top:1562px;width:278px;height:376px;background:linear-gradient(160deg,#ede6df,#e9edf1 60%,#dfe5ec)}
.photo-b{left:461px;top:1562px;width:278px;height:376px;background:linear-gradient(160deg,#3b342e,#8f8578 45%,#5a4f44)}
.contact{left:784px;top:1610px;width:256px;font-size:11px;line-height:22.5px;color:var(--muted)}
.contact h4{margin-top:16px;font-size:11px;font-weight:400;font-style:italic;color:var(--ink);text-transform:uppercase}
.contact .val{font-size:9px;font-style:italic;color:var(--faint);line-height:14px}

/* testimonials */
.testimonials{position:absolute;left:0;top:2012px;width:1200px;height:711px;background:var(--band)}
.eyebrow{top:94px;width:1200px;text-align:center;font-size:14px;color:var(--accent)}
.section-title{top:130px;width:1200px;text-align:center;font-size:42px;font-weight:400}
.avatar{width:74px;height:74px;border-radius:50%;top:257px}
.quote{width:450px;top:372px;text-align:center;font-style:italic;font-size:22px;line-height:45px}
.reviewer{width:450px;top:598px;text-align:center;font-size:15px;text-transform:uppercase}
.role{width:450px;top:626px;text-align:center;font-size:11px;font-style:italic}

/* newsletter */
.news-bg{left:0;top:2723px;width:1200px;height:470px;background:linear-gradient(110deg,#fff 55%,#f6efe8 80%,#e9eee3 100%)}
.news-card{left:162px;top:2798px;width:876px;height:318px;background:#fff;box-shadow:0 2px 10px rgba(0,0,0,.08)}
.news-card h2{position:absolute;left:71px;top:70px;font-size:42px;font-weight:400}
.news-card .sub{position:absolute;left:71px;top:126px;width:380px;text-align:center;font-size:10px;color:var(--faint)}
.field{position:absolute;left:74px;top:208px;width:377px;height:36px;border-bottom:1px solid var(--line)}
.field span{position:absolute;left:0;width:377px;top:8px;text-align:center;font-size:14px;color:var(--faint)}
.field svg{position:absolute;right:0;top:12px}
.cover{position:absolute;left:600px;top:79px;width:203px;height:149px;background:linear-gradient(135deg,#2e9aa3,#e9b23c 60%,#3b8e9a)}
</style>
</head>
<body>

<header class="site-header">
  <nav class="nav">
    <a style="left:159px">Home</a>
    <a class="active" style="left:231px">About</a>
    <a style="left:309px">Storefront</a>
    <a style="left:736px">Coming Soon</a>
    <a style="left:869px">Featured</a>
    <a style="left:973px">Contact</a>
  </nav>
  <div class="logo"><div class="name">MARIANNE</div><div class="tag">AUTHOR &amp; WRITER</div></div>
</header>

<section class="hero" role="img" aria-label="Soft photo of an open book with a pencil">
  <h1>About Me</h1>
  <div class="crumb">Home / <span>About Me</span></div>
</section>

<h2 class="abs intro-title">Welcome To Lorem Ipsum</h2>
<p class="abs intro-sub">Lorem ipsum dolor amet vegan butcher scenester, retro blue</p>
<p class="abs intro-text">Dreamcatcher cornhole subway tile tumeric tbh selvage PBR&amp;B. Fingerstache stumptown godard, man bu butcher echo park pitchfork blue bottle VHS vaporware waistcoat four loko 90's bespoke. Kickstarter flannel vinyl blue bottle sriracha, cloud bread coloring book swag meggings church-key helvetica polaroid subway tile pabst dreamcatcher</p>

<blockquote class="abs pull"><span class="mark">“</span><p>Bolat atom atumptown selfies selvage tilde ullamco lyft raw denim keytar yr mlkshk gochujang mixtape ut master cleanse</p></blockquote>

<p class="abs body-text">Lorem ipsum dolor amet sartorial do marfa distillery meditation cloud bread, laborum asymmetrical whatever quinoa shoreditch in enim. Subway tile shabby chic franzen, id officia microdosing readymade man bun minim neutra craft beer ex flexitarian laboris artisan. Flannel man bun dolore bitters velit 3 wolf moon beard hella drinking vinegar humblebrag narwhal dolore deep v locavore street art. Mixtape vaporware pabst af food truck. Scenester chambray 8-bit taxidermy, typewriter consequat irure affogato portland. Jianbing hexagon yuccie glossier, portland cold-pressed 90's quinoa hashtag velit. Mumblecore gochujang tousled, asymmetrical post-ironic photo booth beard occupy craft beer anim squid live-edge. Eiusmod tumeric nulla butcher brooklyn, veniam selfies fanny pack. Gentrify four dollar toast incididunt, et normcore kogi unicorn church-key laboris cray cornhole PBR&amp;B. Offal aliquip gluten-free in echo park chicharrones vape VHS craft beer. Asymmetrical lo-fi health goth, dolor consequat food truck farm-to-table blog. Truffaut iceland pug, helvetica dolore plaid shoreditch. Organic unicorn commodo, taiyaki vegan flexitarian deep v cloud bread semiotics offal. Stumptown selfies selvage tilde ullamco lyft raw denim keytar yr mlkshk gochujang mixtape ut master cleanse</p>

<div class="abs video" role="img" aria-label="Video still of bookshelves full of colourful books"></div>
<svg class="abs play" width="156" height="156" viewBox="0 0 156 156" aria-label="Play video">
  <circle cx="78" cy="78" r="76" fill="rgba(255,255,255,.25)" stroke="rgba(255,255,255,.55)" stroke-width="3"/>
  <circle cx="78" cy="78" r="57" fill="var(--accent)"/>
  <path d="M68 60 L96 78 L68 96 Z" fill="#fff"/>
</svg>

<div class="abs photo-a" role="img" aria-label="Photo of a hand writing with a fountain pen in a notebook"></div>
<div class="abs photo-b" role="img" aria-label="Photo of a quill in an inkwell beside a handwritten letter"></div>

<div class="abs contact">
  <p>Lorem ipsum dolor sit amet, consectetur cing elit. Suspe ndisse suscipit sagittis leo sit mural estibulum issim alem Lorem ipsum dolor sit amet, AKON lsicn ioifa lkoix consectetur cing elit limat</p>
  <h4 style="margin-top:22px">Address</h4><p class="val">1800 Lorem Ipsum Street Avenue 15</p>
  <h4>Phone Number</h4><p class="val">Mobile Number: +123 456 789 0</p>
  <h4>E-mail</h4><p class="val">email@example.com</p>
</div>

<section class="testimonials">
  <p class="abs eyebrow">TESTIMONIALS</p>
  <h2 class="abs section-title">Read Reviews By My Readers</h2>

  <div class="abs avatar" style="left:336px;background:#8a6a58" role="img" aria-label="Reader portrait"></div>
  <div class="abs avatar" style="left:783px;background:#b7aaa0" role="img" aria-label="Reader portrait"></div>

  <svg class="abs" style="left:95px;top:385px" width="54" height="54" viewBox="0 0 54 54"><circle cx="27" cy="27" r="26" fill="none" stroke="#dedbd4"/><path d="M30 20 L23 27 L30 34" fill="none" stroke="#cfcac2" stroke-width="1.5"/></svg>
  <svg class="abs" style="left:1050px;top:385px" width="54" height="54" viewBox="0 0 54 54"><circle cx="27" cy="27" r="26" fill="#fff"/><path d="M24 20 L31 27 L24 34" fill="none" stroke="var(--accent)" stroke-width="1.5"/></svg>

  <p class="abs quote" style="left:148px">Lamps wayfarers stumptown, and if any intelligentsia butcher pok pok lomo salvia edison bulb bitters asymmetrical lorem ipsum dolor amet ningun</p>
  <p class="abs quote" style="left:595px">Lamps wayfarers stumptown, and if any intelligentsia butcher pok pok lomo salvia edison bulb bitters asymmetrical lorem ipsum dolor amet ningun</p>
  <p class="abs reviewer" style="left:148px">Lena Marlowe</p>
  <p class="abs role" style="left:148px">Reporter/Publisher</p>
  <p class="abs reviewer" style="left:595px">Owen Fairley</p>
  <p class="abs role" style="left:595px">Reporter/Publisher</p>
</section>

<div class="abs news-bg" role="img" aria-label="Soft desk scene with a notebook and a plant"></div>
<section class="abs news-card">
  <h2>Join The Newsletter</h2>
  <p class="sub">Subscribe To Get In Touch</p>
  <div class="field"><span>Enter Your E-mail</span>
    <svg width="16" height="10" viewBox="0 0 16 10"><path d="M1 5 H14 M10 1 L14 5 L10 9" fill="none" stroke="#888" stroke-width="1.2"/></svg>
  </div>
  <div class="cover" role="img" aria-label="Stack of copies of the book"></div>
</section>

</body>
</html>
```